Book Cover for Productivity Book

I need a book cover for my latest publication "On Momentum: The Gathered Insights of the Most Tireless Woman Living"

You can see my branding at www.brightvarno.com

This is meant to be my epic pinaccle work on productivity, I want it to look like the end all be all word on productivity.

Target Market(s)

entrepreneurs

```html
<!DOCTYPE html>
<html lang="en">
<head>
<meta charset="utf-8">
<title>On Momentum – Book Cover</title>
<link rel="stylesheet" href="https://fonts.googleapis.com/css2?family=Oswald:wght@400;500;600&display=swap">
<style>
  :root {
    --backdrop: #2b2a28;
    --paper-light: #f4f4f3;
    --paper-mid: #d9d9d8;
    --paper-dark: #bdbdbc;
    --ink: #1a1a1a;
    --accent: #d41f26;
  }
  * { margin: 0; padding: 0; box-sizing: border-box; }
  html, body {
    width: 1200px;
    height: 1200px;
    overflow: hidden;
    background: var(--backdrop);
  }
  .cover {
    position: absolute;
    left: 211px;
    top: 30px;
    width: 778px;
    height: 1140px;
    background:
      radial-gradient(ellipse at 30% 20%, rgba(255,255,255,0.55), transparent 55%),
      radial-gradient(ellipse at 75% 85%, rgba(255,255,255,0.45), transparent 50%),
      radial-gradient(ellipse at 15% 70%, rgba(0,0,0,0.10), transparent 45%),
      radial-gradient(ellipse at 85% 30%, rgba(0,0,0,0.08), transparent 45%),
      linear-gradient(160deg, var(--paper-mid), var(--paper-light) 45%, var(--paper-dark));
    font-family: "Oswald", "Arial Narrow", sans-serif;
    color: var(--ink);
  }
  .title {
    position: absolute;
    left: 58px;
    top: 130px;
    width: 660px;
    height: 340px;
    display: flex;
    align-items: flex-end;
    justify-content: flex-end;
    line-height: 0.78;
  }
  .title__lead {
    font-size: 68px;
    font-weight: 500;
    color: var(--ink);
    margin-right: 14px;
    transform: scaleY(1.05);
    transform-origin: bottom;
  }
  .title__main {
    display: flex;
    align-items: flex-end;
    color: var(--accent);
    font-weight: 500;
    font-size: 112px;
  }
  .title__main span {
    display: inline-block;
    transform-origin: bottom;
    margin-left: 3px;
  }
  .rule {
    position: absolute;
    left: 112px;
    top: 565px;
    width: 578px;
    height: 3px;
    background: var(--accent);
  }
  .subtitle {
    position: absolute;
    left: 0;
    top: 640px;
    width: 778px;
    text-align: center;
    font-weight: 400;
    font-size: 54px;
    line-height: 76px;
    text-transform: uppercase;
    letter-spacing: 0.5px;
  }
  .subtitle__small { font-size: 42px; }
  .author {
    position: absolute;
    left: 0;
    top: 975px;
    width: 778px;
    text-align: center;
    font-weight: 600;
    font-size: 62px;
    letter-spacing: 1px;
    text-transform: uppercase;
  }
</style>
</head>
<body>
  <main class="cover">
    <h1 class="title">
      <span class="title__lead">ON</span>
      <span class="title__main">
        <span style="transform:scaleY(1.0)">M</span>
        <span style="transform:scaleY(1.3)">O</span>
        <span style="transform:scaleY(1.6)">M</span>
        <span style="transform:scaleY(1.9)">E</span>
        <span style="transform:scaleY(2.2)">N</span>
        <span style="transform:scaleY(2.55)">T</span>
        <span style="transform:scaleY(2.9)">U</span>
        <span style="transform:scaleY(3.25)">M</span>
      </span>
    </h1>
    <div class="rule"></div>
    <p class="subtitle">
      The Gathered Insights of the<br>
      <span class="subtitle__small">Most</span> Tireless Woman Living
    </p>
    <p class="author">Dana Korvel</p>
  </main>
</body>
</html>
```